Marlow Family Chiropractic Stationary

The letterhead and business card must have our logo.
We would like to see the logo used in different ways ( It can be expanded upon in the stationary.)
Please use the the same or similar colors.
Must be eye catching and memorable.
Must be easy to read

Reason: The doctor has been too busy to make any final decisions. He would like to give himself a little more time.

Target Market(s)

Chiropractic Healthcare

Industry/Entity Type

Business

Requirements
Must have
• Dr. Nathaniel Marlow D.C.
Chiropractor

860-555-0193

415 Birchwood Parkway, 2nd Floor
Vernon, CT 06099

drmarlow@marlowspine.example
www.marlowspine.example
www.facebook.com/MarlowFamilySpine
Should not have
• should not be difficult to read

```html
<!DOCTYPE html>
<html lang="en">
<head>
<meta charset="utf-8">
<title>Marlow Family Chiropractic – Business Cards</title>
<link rel="stylesheet" href="https://fonts.googleapis.com/css2?family=Montserrat:wght@600&family=Arimo:wght@400;700&display=swap">
<style>
  :root {
    --stage: #b9b9b9;
    --ink: #050505;
    --lime: #a6cf5c;
    --leaf: #2a9647;
    --gold: #c2a834;
    --olive: #5e6a38;
    --white: #ffffff;
    --charcoal: #2b2b2b;
  }
  * { margin: 0; padding: 0; box-sizing: border-box; }
  html, body { width: 1200px; height: 721px; overflow: hidden; }
  body { background: var(--stage); position: relative; font-family: "Arimo", Arial, sans-serif; }

  .card { position: absolute; width: 524px; height: 300px; overflow: hidden; }
  .card--front-detail { left: 54px; top: 38px; background: var(--ink); }
  .card--back-lime { left: 611px; top: 38px; background: var(--lime); }
  .card--front-brand { left: 54px; top: 370px; background: var(--ink); }
  .card--back-green { left: 608px; top: 370px; background: var(--leaf); }

  .wordmark {
    position: absolute;
    font-family: "Montserrat", Arial, sans-serif;
    font-weight: 600;
    text-transform: uppercase;
    text-align: center;
    line-height: 1;
  }
  .wordmark__name, .wordmark__tag { display: block; }

  .card--front-detail .wordmark { left: 30px; top: 163px; width: 222px; color: var(--lime); }
  .card--front-detail .wordmark__name { font-size: 34px; }
  .card--front-detail .wordmark__tag { font-size: 14px; margin-top: 8px; }

  .card--back-lime .wordmark,
  .card--back-green .wordmark { left: 0; right: 0; top: 112px; color: var(--white); }
  .card--back-lime .wordmark__name,
  .card--back-green .wordmark__name { font-size: 40px; }
  .card--back-lime .wordmark__tag,
  .card--back-green .wordmark__tag { font-size: 18px; margin-top: 10px; }

  .card--front-brand .wordmark { left: 0; right: 0; top: 97px; color: var(--lime); }
  .card--front-brand .wordmark__name { font-size: 66px; }
  .card--front-brand .wordmark__tag { font-size: 27px; margin-top: 14px; }

  .wave-band {
    position: absolute; left: 0; right: 0; top: 205px; bottom: 0;
    background: linear-gradient(to right, #1a1a12 0%, var(--olive) 35%, var(--lime) 62%);
  }

  .doctor { position: absolute; right: 14px; top: 29px; text-align: right; }
  .doctor__name { color: var(--lime); font-weight: 700; font-size: 15px; }
  .doctor__role { color: var(--gold); font-size: 14px; margin-top: 7px; }
  .address { position: absolute; right: 14px; top: 106px; text-align: right; color: var(--white); font-size: 13px; line-height: 1.35; }

  .contacts { position: absolute; right: 14px; top: 212px; list-style: none; text-align: right; color: var(--charcoal); font-size: 13px; line-height: 19.5px; }
  .contacts li { display: flex; justify-content: flex-end; align-items: center; gap: 5px; }
  .contacts svg { width: 10px; height: 10px; flex: none; }
  .icon-square { width: 9px; height: 9px; background: #3b5b98; flex: none; }

  .site {
    position: absolute; left: 0; right: 0; bottom: 28px;
    text-align: center; font-size: 15px; letter-spacing: 2.2px;
  }
  .card--back-lime .site { color: var(--charcoal); bottom: 22px; }
  .card--front-brand .site, .card--back-green .site { color: var(--white); }
</style>
</head>
<body>

<section class="card card--front-detail">
  <div class="wave-band" role="img" aria-label="Decorative flowing wave band in black, gold, taupe and lime"></div>
  <div class="wordmark"><span class="wordmark__name">Marlow</span><span class="wordmark__tag">Family Chiropractic</span></div>
  <div class="doctor">
    <p class="doctor__name">Dr. Nathaniel Marlow D.C.</p>
    <p class="doctor__role">Chiropractor</p>
  </div>
  <p class="address">415 Birchwood Parkway<br>2nd Floor, Vernon, CT 06099</p>
  <ul class="contacts">
    <li><svg viewBox="0 0 10 10"><path d="M2 1 L4 1 L4.5 3.5 L3.3 4.3 C4 5.8 4.5 6.3 5.8 6.8 L6.6 5.5 L9 6 L9 8 C9 8.8 8 9.2 7 9 C4 8 2 6 1 3 C0.8 2 1.2 1 2 1 Z" fill="none" stroke="var(--charcoal)" stroke-width="1"/></svg>860-555-0193</li>
    <li><span class="icon-square"></span>MarlowFamilySpine</li>
    <li><svg viewBox="0 0 10 10"><circle cx="5" cy="5" r="4.2" fill="none" stroke="var(--charcoal)"/><ellipse cx="5" cy="5" rx="1.8" ry="4.2" fill="none" stroke="var(--charcoal)" stroke-width=".8"/><line x1="0.8" y1="5" x2="9.2" y2="5" stroke="var(--charcoal)" stroke-width=".8"/></svg>www.marlowspine.example</li>
    <li><svg viewBox="0 0 10 10"><rect x="0.8" y="2" width="8.4" height="6" fill="none" stroke="var(--charcoal)"/><path d="M0.8 2 L5 5.5 L9.2 2" fill="none" stroke="var(--charcoal)"/></svg>drmarlow@marlowspine.example</li>
  </ul>
</section>

<section class="card card--back-lime">
  <div class="wordmark"><span class="wordmark__name">Marlow</span><span class="wordmark__tag">Family Chiropractic</span></div>
  <p class="site">www.marlowspine.example</p>
</section>

<section class="card card--front-brand">
  <div class="wordmark"><span class="wordmark__name">Marlow</span><span class="wordmark__tag">Family Chiropractic</span></div>
  <p class="site">www.marlowspine.example</p>
</section>

<section class="card card--back-green">
  <div class="wordmark"><span class="wordmark__name">Marlow</span><span class="wordmark__tag">Family Chiropractic</span></div>
  <p class="site">www.marlowspine.example</p>
</section>

</body>
</html>
```